Dredging Contractors, we run amphibious walking dredges cleaning up waterways, mines etc

We need an updated web design for our company based in Australia.
We have 20t "Walking" amphibious excavators that service mining companies and governments, cleaning up waterways and pond systems.
We would like to see designs that reflect our cutting edge marine / technology that appeals to our engineering / civil / mining clients. As well as providing benefits by cleaning up our marine waterways.
We have an existing web page at www.marshtrekworks.com.au

Target Market(s)

Mining companies, engineers, council civil engineers, developers, waterways engineers

Industry/Entity Type

It Company

Requirements
Must have
• Logo, contact details, Photos of equipment page (Gallery), quotation page, Contact page, list of capabilities page (Products and services),

```html
<!DOCTYPE html>
<html lang="en">
<head>
<meta charset="utf-8">
<title>Marshtrek Works – Amphibious Dredging</title>
<link rel="stylesheet" href="https://fonts.googleapis.com/css2?family=Lato:wght@400;700&family=Arimo:wght@400;700&display=swap">
<style>
  :root {
    --teal: #0e98a4;
    --teal-dark: #0a7d87;
    --teal-light: #d9f3f6;
    --cyan: #19c6d4;
    --ink: #1d1d1d;
    --text: #333;
    --line: #d6d6d6;
    --photo-sky: #7aa9d6;
    --photo-green: #5e8466;
    --photo-water: #6f8790;
    --photo-earth: #8b8170;
    --bg: #ffffff;
  }
  * { box-sizing: border-box; margin: 0; padding: 0; }
  html, body { width: 714px; height: 1200px; overflow: hidden; background: var(--bg); }
  body { position: relative; font-family: "Lato", sans-serif; color: var(--text); }
  .abs { position: absolute; }

  .top-bar { left: 0; top: 0; width: 714px; height: 6px; background: var(--teal); }
  .quote-tab { left: 586px; top: 6px; width: 60px; height: 15px; background: var(--teal); color: #fff;
    font-size: 7.5px; line-height: 15px; text-align: center; }

  .brand { left: 48px; top: 33px; display: flex; align-items: center; gap: 8px; }
  .brand-mark { width: 46px; height: 46px; border-radius: 50%; background: var(--teal); }
  .brand-name { font-family: "Arimo", sans-serif; font-weight: 700; font-size: 20px; line-height: 19px; color: var(--ink); letter-spacing: .5px; }

  .search { left: 495px; top: 45px; width: 171px; height: 27px; border: 1px solid #9a9a9a; border-radius: 3px;
    background: linear-gradient(#f3f3f3, #e2e2e2); }
  .search span { position: absolute; left: 9px; top: 8px; font-size: 8px; color: #444; font-family: "Arimo", sans-serif; }
  .search-btn { position: absolute; right: 2px; top: 2px; width: 23px; height: 21px; border: 1px solid #777; border-radius: 2px;
    background: linear-gradient(#eee, #bbb); }

  .nav { left: 45px; top: 100px; width: 624px; height: 28px; display: flex; border-radius: 3px; overflow: hidden;
    background: linear-gradient(var(--teal) 0%, var(--teal-dark) 100%); }
  .nav a { flex: 1; text-align: center; line-height: 28px; color: #fff; font-family: "Arimo", sans-serif; font-weight: 700;
    font-size: 9px; text-decoration: none; border-right: 1px solid rgba(255,255,255,.25); }
  .nav a:last-child { border-right: 0; }
  .nav a.active { background: linear-gradient(#fff, var(--teal-light)); color: var(--teal); border: 1px solid var(--teal); }
  .nav a.soft { font-weight: 400; color: #d9f6f8; }

  .photo { background: linear-gradient(var(--photo-sky), var(--photo-green)); }
  .hero { left: 44px; top: 157px; width: 624px; height: 325px; box-shadow: 0 6px 8px -4px rgba(0,0,0,.35); }
  .dots { left: 336px; top: 490px; display: flex; gap: 2px; }
  .dots i { width: 8px; height: 8px; border-radius: 50%; background: #d8d8d8; border: 1px solid #aaa; }
  .dots i.on { background: #777; }

  .rule { height: 1px; background: var(--line); }
  .shade { height: 14px; background: radial-gradient(ellipse at 50% 100%, rgba(0,0,0,.12), transparent 70%); }

  .intro { left: 52px; top: 554px; width: 610px; text-align: center; font-size: 9px; line-height: 13px; color: var(--ink); }
  .dark-btn { left: 317px; top: 605px; width: 73px; height: 22px; }
  .dark-btn span { position: absolute; left: 0; top: 0; width: 66px; height: 22px; line-height: 22px; text-align: center;
    color: #eee; font-family: "Arimo", sans-serif; font-size: 8px; }

  .section-title { font-size: 11px; color: var(--ink); }
  .pager { display: flex; gap: 2px; }
  .pager b { width: 19px; height: 17px; border-radius: 4px; background: linear-gradient(#fafafa, #d5d5d5);
    border: 1px solid #c4c4c4; display: flex; align-items: center; justify-content: center; }

  .thumb { border: 1px solid #ccc; padding: 3px; background: #fff; }
  .thumb div { width: 100%; height: 100%; }
  .card-title { font-size: 11px; color: var(--ink); text-align: center; }
  .card-text { font-size: 7.9px; line-height: 12.8px; color: var(--text); text-align: center; }
  .pill { height: 25px; border-radius: 13px; background: linear-gradient(#ddd, #aaa); padding: 3px; }
  .pill div { height: 100%; border-radius: 10px; background: linear-gradient(#3fe0ea, var(--cyan) 60%, #12a9b6);
    display: flex; align-items: center; justify-content: space-between; padding: 0 8px 0 12px;
    font-family: "Arimo", sans-serif; font-size: 9px; color: #0d2f33; }
  .pill i { width: 10px; height: 10px; border-radius: 50%; background: #143b40; }

  .gallery-item { border: 1px solid #bbb; box-shadow: 0 5px 6px -3px rgba(0,0,0,.3); }

  .footer-links { left: 47px; top: 1154px; font-size: 7.5px; color: var(--ink); }
  .footer-links span { padding: 0 3px; }
  .copy { left: 44px; top: 1178px; font-size: 7.3px; color: var(--ink); }
  .social { left: 539px; top: 1155px; display: flex; gap: 6px; }
  .social i { width: 29px; height: 29px; border-radius: 5px; background: linear-gradient(#e8e8e8, #bdbdbd); }
</style>
</head>
<body>
  <div class="abs top-bar"></div>
  <div class="abs quote-tab">Get a free quote</div>

  <div class="abs brand">
    <div class="brand-mark"></div>
    <div class="brand-name">MARSHTREK<br>WORKS</div>
  </div>

  <div class="abs search">
    <span>Search</span>
    <div class="search-btn">
      <svg width="21" height="19" viewBox="0 0 21 19"><circle cx="9" cy="8" r="4.5" fill="none" stroke="#333" stroke-width="2"/><line x1="12" y1="11" x2="16" y2="15" stroke="#333" stroke-width="2.5"/></svg>
    </div>
  </div>

  <nav class="abs nav">
    <a class="active">HOME</a><a>ABOUT US</a><a>PRODUCTS</a><a>SERVICES</a><a class="soft">QUOTATION</a><a>NEWS LETTER</a><a>CONTACT US</a>
  </nav>

  <div class="abs hero photo" role="img" aria-label="Photo: amphibious walking dredge lifted by a crane"></div>
  <div class="abs dots"><i class="on"></i><i></i><i></i><i></i></div>

  <div class="abs shade" style="left:140px;top:524px;width:430px;"></div>
  <div class="abs rule" style="left:46px;top:538px;width:624px;"></div>

  <p class="abs intro">Marshtrek Works has been working as waterways engineers since 1995.Our amphibious dredges are highly mobile and is easily transported by truck to anywhere in Australia.Our portable dewatering systems enable us to pump straight from the dredge and dry material down to 25 microns.We are able to dredge small ponds or marinas&nbsp; to mine sludge or industrial dewatering projects.</p>

  <div class="abs dark-btn">
    <svg width="73" height="22" viewBox="0 0 73 22"><path d="M3 0H65L73 11L65 22H3Q0 22 0 19V3Q0 0 3 0Z" fill="#3a3a3a" stroke="#222"/></svg>
    <span>READ MORE</span>
  </div>

  <div class="abs rule" style="left:40px;top:635px;width:634px;"></div>

  <div class="abs section-title" style="left:47px;top:654px;">Services</div>
  <div class="abs pager" style="left:626px;top:652px;">
    <b><svg width="8" height="10"><path d="M6 1L2 5L6 9" stroke="#222" stroke-width="2" fill="none"/></svg></b>
    <b><svg width="8" height="10"><path d="M2 1L6 5L2 9" stroke="#222" stroke-width="2" fill="none"/></svg></b>
  </div>
  <div class="abs rule" style="left:46px;top:674px;width:624px;"></div>

  <div class="abs thumb" style="left:71px;top:692px;width:149px;height:112px;"><div class="photo" role="img" aria-label="Photo: dredge working in a mine pond"></div></div>
  <div class="abs thumb" style="left:282px;top:692px;width:149px;height:112px;"><div class="photo" role="img" aria-label="Photo: dredge discharge over a waterway"></div></div>
  <div class="abs thumb" style="left:489px;top:692px;width:149px;height:112px;"><div class="photo" role="img" aria-label="Photo: dredge working in a harbour pond"></div></div>

  <div class="abs card-title" style="left:71px;top:811px;width:149px;">Mining companies</div>
  <div class="abs card-title" style="left:262px;top:811px;width:189px;">Cleaning up waterways</div>
  <div class="abs card-title" style="left:489px;top:811px;width:149px;">Ponds</div>

  <p class="abs card-text" style="left:66px;top:832px;width:172px;">Lorem ipsum dolor sit amet, consectetuer adip iscing elit, sed diam nonummy nibh euismoinc iunt ut laoreet dolore magna aliquam erat volu tpat. Ut wisi enim ad minim veniam, quis</p>
  <p class="abs card-text" style="left:275px;top:832px;width:172px;">Lorem ipsum dolor sit amet, consectetuer adip iscing elit, sed diam nonummy nibh euismoinc iunt ut laoreet dolore magna aliquam erat volu tpat. Ut wisi enim ad minim veniam, quis</p>
  <p class="abs card-text" style="left:485px;top:832px;width:172px;">Lorem ipsum dolor sit amet, consectetuer adip iscing elit, sed diam nonummy nibh euismoinc iunt ut laoreet dolore magna aliquam erat volu tpat. Ut wisi enim ad minim veniam, quis</p>

  <div class="abs pill" style="left:114px;top:898px;width:86px;"><div>Read more<i></i></div></div>
  <div class="abs pill" style="left:320px;top:897px;width:86px;"><div>Read more<i></i></div></div>
  <div class="abs pill" style="left:532px;top:897px;width:86px;"><div>Read more<i></i></div></div>

  <div class="abs section-title" style="left:48px;top:955px;">Gallery</div>
  <div class="abs pager" style="left:623px;top:952px;">
    <b><svg width="8" height="10"><path d="M6 1L2 5L6 9" stroke="#222" stroke-width="2" fill="none"/></svg></b>
    <b><svg width="8" height="10"><path d="M2 1L6 5L2 9" stroke="#222" stroke-width="2" fill="none"/></svg></b>
  </div>
  <div class="abs rule" style="left:46px;top:976px;width:624px;"></div>

  <div class="abs gallery-item photo" style="left:54px;top:986px;width:135px;height:116px;" role="img" aria-label="Photo: dredge on a riverbank"></div>
  <div class="abs gallery-item photo" style="left:214px;top:986px;width:136px;height:116px;" role="img" aria-label="Photo: dredge hull on a truck"></div>
  <div class="abs gallery-item photo" style="left:370px;top:986px;width:138px;height:116px;" role="img" aria-label="Photo: dewatering equipment on site"></div>
  <div class="abs gallery-item photo" style="left:522px;top:986px;width:137px;height:116px;" role="img" aria-label="Photo: dredge working in a lake"></div>

  <div class="abs shade" style="left:40px;top:1120px;width:634px;"></div>
  <div class="abs rule" style="left:46px;top:1133px;width:624px;"></div>

  <div class="abs footer-links">HOME<span>|</span>ABOUT US<span>|</span>PRODUCTS<span>|</span>SERVICES<span>|</span>QUOTATION<span>|</span>NEWS LETTER<span>|</span>CONTACT US</div>
  <div class="abs copy">2013 Copyrights. All Rights Reserved.</div>

  <div class="abs social">
    <i role="img" aria-label="Social network link"></i>
    <i role="img" aria-label="Social network link"></i>
    <i role="img" aria-label="Photo sharing link"></i>
  </div>
</body>
</html>
```